Brochure to advertise our unique physiotherapy clinic to general practitioners

We want to advertise our unique physiotherapy clinic to general practitioners (GPs) to develop there awareness of both our existence and services offered. The brochure should highlight our uniqueness (i.e. providing the highest quality care, advice and education) based on our expert research-based knowledge and skills. After reading the brochure, we want GPs to feel like they know us a little and feel happy to refer their patients to our clinic.
Attached is a draft flyer containing our logo, contact details, profile pictures and the information we would like to be contained in the brochure. We would like the brochure to be A4 double sided and able to be folded to fit into an envelope. More material (pictures) and understanding of our clinic can be found at www.kinetrova.com.au

A brief background of our team:
Our team currently consists of two physiotherapists specialising in the management of musculoskeletal and sports injuries, Dr Martin Hollowby and Dr Gareth Lindqvist. Both Martin and Gareth have completed PhDs related to musculosketal injury management, and continue to be actively involved in international research groups. Between them they have authored more than 50 peer reviewed papers, presented at countless national and international conferences, and coordinate numerous courses to facilitate professional development of other clinicians. Most importantly, they continue to enjoy mixing these research and teaching activities with treating patients.

Reason: Consultation with clinic partner is needed and to allow time for modifications and additional designs. We will pick one, just want quality.
Thanks

Thank you for some great designs thus far everyone. We have decided to remove the fees from the brochure so please do the same for any future submissions. In the process of trying to provide feedback now.
Thanks
Reason: A couple of designs are close and we want to allow time to make appropriate modifications. This will be the last extension. Thanks for everyones effort so far

Target Market(s)
Australian General Practitioners and other health professionals are the targeted audience
Industry/Entity Type
Clinic
Look and feel

```html
<!DOCTYPE html>
<html lang="en">
<head>
<meta charset="utf-8">
<title>Kinetrova Brochure</title>
<link rel="stylesheet" href="https://fonts.googleapis.com/css2?family=Noto+Serif:wght@400&family=Open+Sans:wght@400&display=swap">
<style>
  :root {
    --backdrop: #e8e5e1;
    --paper: #f3f3f5;
    --brand-blue: #00a9e8;
    --band-blue: #1b90cf;
    --band-lime: #dce02c;
    --pill-green: #8cc63f;
    --ink: #111111;
    --logo-grey: #5a5a5a;
    --photo-a: #8a8d86;
    --photo-b: #6f8a55;
    --photo-c: #9aa3ad;
    --badge-bg: #ffffff;
  }
  * { box-sizing: border-box; margin: 0; padding: 0; }
  html, body { width: 1200px; height: 1000px; overflow: hidden; }
  body {
    position: relative;
    background: var(--backdrop);
    font-family: "Noto Serif", serif;
    color: var(--ink);
  }
  .page {
    position: absolute;
    width: 508px;
    height: 718px;
    background: var(--paper);
    box-shadow: 4px 6px 10px rgba(0,0,0,0.35);
    overflow: hidden;
  }
  .page--front { left: 20px; top: 228px; }
  .page--back { left: 625px; top: 232px; width: 507px; }
  .top-band {
    position: absolute; left: 0; top: 0; width: 100%; height: 18px;
    background: var(--band-blue);
  }
  .top-band__accent {
    position: absolute; left: 168px; top: 0; width: 169px; height: 18px;
    background: var(--band-lime);
  }
  .swoosh { position: absolute; left: 0; top: 0; width: 100%; height: 100%; }
  .logo-box {
    position: absolute; left: 5px; top: 20px; width: 210px; height: 86px;
    background: #ffffff;
    display: flex; align-items: center; gap: 10px; padding-left: 22px;
  }
  .logo-box__dot { width: 20px; height: 20px; border-radius: 50%; background: var(--brand-blue); }
  .logo-box__name { font-size: 22px; color: var(--logo-grey); }
  .content { position: absolute; font-size: 11.3px; line-height: 13.6px; }
  .section-title { font-size: 23px; line-height: 26px; font-weight: 400; }
  .clinic { left: 62px; top: 118px; width: 430px; }
  .team { left: 62px; top: 255px; width: 430px; }
  .services { left: 60px; top: 429px; width: 440px; }
  .services__line { display: block; white-space: nowrap; }
  .photo { position: absolute; }
  .photo--martin { left: 248px; top: 547px; width: 116px; height: 77px; background: linear-gradient(135deg, var(--photo-a), #b8b6ad); }
  .photo--gareth { left: 369px; top: 547px; width: 106px; height: 77px; background: linear-gradient(135deg, var(--photo-b), #a9bf8a); }
  .caption { position: absolute; top: 635px; font-family: "Open Sans", sans-serif; font-size: 7.5px; text-align: center; }
  .caption--martin { left: 248px; width: 116px; }
  .caption--gareth { left: 369px; width: 106px; }

  .intro { left: 37px; top: 118px; width: 430px; line-height: 15.4px; }
  .intro__lead { font-size: 26px; }
  .conditions { left: 37px; top: 253px; width: 440px; line-height: 15.4px; }
  .conditions ul { list-style: none; }
  .conditions li { position: relative; line-height: 15.4px; }
  .conditions li::before { content: "·"; position: absolute; left: -28px; }
  .conditions li.tight::before { left: -6px; }
  .pill {
    position: absolute; left: 133px; top: 540px; width: 349px; height: 28px;
    border-radius: 14px; background: var(--pill-green);
    font-family: "Open Sans", sans-serif; font-size: 18.5px; line-height: 28px;
    text-align: center; color: var(--ink);
  }
  .partner-badge {
    position: absolute; left: 260px; top: 603px; width: 134px; height: 63px;
    background: var(--badge-bg);
    display: flex; align-items: center; justify-content: center;
  }
  .partner-badge__shape { width: 110px; height: 18px; background: #3a3a3a; border-radius: 2px; }
  .photo--clinic { left: 400px; top: 603px; width: 85px; height: 63px; background: linear-gradient(135deg, var(--photo-c), #e6e8ea); }
</style>
</head>
<body>

<section class="page page--front">
  <div class="top-band"><div class="top-band__accent"></div></div>
  <svg class="swoosh" viewBox="0 0 508 718" preserveAspectRatio="none" aria-hidden="true">
    <path d="M0,112 C0,450 40,650 508,712 L508,718 L0,718 Z" fill="var(--brand-blue)"/>
  </svg>
  <div class="logo-box"><span class="logo-box__dot"></span><span class="logo-box__name">Kinetrova</span></div>

  <div class="content clinic">
    <h2 class="section-title">The Clinic</h2>
    <p>We are a very unique and progressive physiotherapy clinic at Kinetrova. Our clinic is located within Meridian Fitness, Level 4, 13-14, Calder Avenue, Ashbury East, VIC, 3190. Further information about us is detailed below. Additionally, please visit our website and join the associated ‘tendinopathy’ ‘patellofemoral’ and ‘biomechanics’ blogs if you are interested at: http://www.kinetrova.com.au/</p>
  </div>

  <div class="content team">
    <h2 class="section-title">Who are we?</h2>
    <p>Our team currently consists of two physiotherapists specialising in the management of musculoskeletal and sports injuries, Dr Martin Hollowby and Dr Gareth Lindqvist. Both Martin and Gareth have completed PhDs related to musculosketal injury management, and continue to be actively involved in international research groups. Between them they have authored more than 40 peer reviewed papers, presented at countless national and international conferences, and coordinate numerous courses to facilitate professional development of other clinicians. Most importantly, they continue to enjoy mixing these research and teaching activities with treating patients.</p>
  </div>

  <div class="content services">
    <h2 class="section-title" style="padding-left:2px">Services offered</h2>
    <p>
      <span class="services__line" style="padding-left:8px">All patients receive the highest quality 1-1 physiotherapy treatment and we</span>
      <span class="services__line" style="padding-left:4px">offer patients accurate, realistic and lasting solution to their problems. We</span>
      <span class="services__line" style="padding-left:5px">can guarantee the quality of our treatment because we are genuine experts</span>
      <span class="services__line" style="padding-left:23px">in managing difficult injuries, with a wealth of clinical and research</span>
      <span class="services__line" style="padding-left:28px">experience. This ultimately means we can more effective care, saving</span>
      <span class="services__line" style="padding-left:36px">patients both time and money.</span>
    </p>
  </div>

  <div class="photo photo--martin" role="img" aria-label="Portrait photo of Dr Martin Hollowby"></div>
  <div class="photo photo--gareth" role="img" aria-label="Portrait photo of Dr Gareth Lindqvist"></div>
  <p class="caption caption--martin">Dr Martin Hollowby</p>
  <p class="caption caption--gareth">Dr Gareth Lindqvist</p>
</section>

<section class="page page--back">
  <div class="top-band"><div class="top-band__accent"></div></div>
  <svg class="swoosh" viewBox="0 0 507 718" preserveAspectRatio="none" aria-hidden="true">
    <path d="M0,108 C0,450 45,650 507,712 L507,718 L0,718 Z" fill="var(--brand-blue)"/>
  </svg>
  <div class="logo-box"><span class="logo-box__dot"></span><span class="logo-box__name">Kinetrova</span></div>

  <div class="content intro">
    <p><span class="intro__lead">We</span> have the facilities, knowledge and skills to complete comprehensive biomechanical assessments, evidence based exercise prescription, access to a full gym, highly effective manual therapy techniques, dry needling, diagnostic ultrasound, shockwave therapy, and foot orthoses advice/prescription. Put together, this will ensure all patients who attend our clinic an optimal recovery from almost any musculoskeletal injury, whether acute or chronic.</p>
  </div>

  <div class="content conditions">
    <p>We treat injuries others cannot fix</p>
    <p>We have a reputation for successfully managing injuries that are difficult, or unresolving, including:</p>
    <ul>
      <li style="margin-left:31px">Achilles tendinopathy</li>
      <li style="margin-left:31px">Patellar tendinopathy</li>
      <li style="margin-left:31px">Tennis elbow</li>
      <li style="margin-left:31px">Rotator cuff injury</li>
      <li style="margin-left:31px">Hamstring origin tendinopathy</li>
      <li style="margin-left:31px">Tibialis posterior tendon injury</li>
      <li style="margin-left:31px">Plantar fasciitis</li>
      <li style="margin-left:31px">Iliotibial band syndrome ·&nbsp;&nbsp;&nbsp;&nbsp;&nbsp;&nbsp;Patellofemoral joint injury</li>
      <li class="tight" style="margin-left:31px">Back and neck pain</li>
      <li style="margin-left:62px">Chronic strains and sprains</li>
      <li style="margin-left:62px">Shoulder pain</li>
      <li style="margin-left:62px">Groin pain</li>
      <li style="margin-left:62px">Hip impingement</li>
      <li class="tight" style="margin-left:62px">Stress fractures</li>
      <li style="margin-left:93px">Shin splints (exercise induced leg pain)</li>
    </ul>
  </div>

  <div class="pill">All treatment sessions are 30 minutes</div>

  <div class="partner-badge" role="img" aria-label="Partner claims badge"><span class="partner-badge__shape"></span></div>
  <div class="photo photo--clinic" role="img" aria-label="Photo of a physiotherapist at work in the clinic"></div>
</section>

</body>
</html>
```